I would like a site similar to this: http://www.givewheelsforheroes.example

old site: http://www.autosforpatriots.example

Create a professional website; a car donation site seeking leads to return calls.

Please see http://www.givewheelsforheroes.example for the concept I am after.

The webpage should have a professional feel. The pages to include are 'Home', 'About us' and 'Get Started'

Industry/Entity Type

It Professional

Coding

Coded - Design and coding required

Number of Pages Required

1 page

```html
<!DOCTYPE html>
<html lang="en">
<head>
<meta charset="utf-8">
<title>Autos for Patriots – Donate Your Car</title>
<link href="https://fonts.googleapis.com/css2?family=Roboto+Slab:wght@400;500;600&family=Open+Sans:wght@400;600;700&family=Lato:wght@400;700&display=swap" rel="stylesheet">
<style>
:root{
  --navy:#0a2259;
  --navy-panel:#1f2452;
  --blue:#1a75bb;
  --blue-section:#0f74b9;
  --red:#a3150f;
  --page:#efefef;
  --white:#ffffff;
  --text-grey:#7a7a7a;
  --text-dark:#555555;
  --footer:#524c4c;
  --line:#d6d6d6;
}
*{box-sizing:border-box;margin:0;padding:0}
html,body{width:1200px;height:2267px;overflow:hidden}
body{background:var(--page);font-family:"Open Sans",Arial,sans-serif;position:relative;color:var(--text-dark)}
a{color:inherit;text-decoration:none}

.top-bar{position:absolute;left:0;top:0;width:1200px;height:46px;background:var(--navy);color:var(--white);font-size:14px;font-weight:700}
.top-bar .help-links{position:absolute;left:100px;top:13px;display:flex;align-items:center}
.top-bar .help-links span{padding:0 18px;border-left:1px solid rgba(255,255,255,.6)}
.top-bar .help-links span:first-child{padding-left:0;border-left:none}
.top-bar .call{position:absolute;right:100px;top:11px;display:flex;align-items:center;gap:12px}
.top-bar .call .phone-box{width:24px;height:24px;background:var(--white);border-radius:4px;display:flex;align-items:center;justify-content:center}

.brand{position:absolute;left:100px;top:82px;display:flex;align-items:center;gap:12px}
.brand .brand-mark{width:30px;height:30px;background:var(--red);border-radius:4px}
.brand .brand-name{font-family:"Open Sans",sans-serif;font-weight:700;font-size:26px;color:var(--navy)}
.hours{position:absolute;left:760px;width:340px;top:74px;text-align:center;font-family:"Open Sans",sans-serif;font-size:26px;line-height:30px;color:var(--navy)}

.main-nav{position:absolute;left:100px;top:171px;width:692px;height:53px;background:var(--blue);display:flex;border-radius:6px 0 0 0}
.main-nav a{flex:0 0 auto;display:flex;align-items:center;justify-content:center;color:var(--white);font-family:"Open Sans",sans-serif;font-weight:700;font-size:15px;letter-spacing:1px;border-right:1px solid rgba(255,255,255,.5)}
.main-nav a:nth-child(1){width:220px}
.main-nav a:nth-child(2){width:233px}
.main-nav a:nth-child(3){width:239px;border-right:none}

.hero{position:absolute;left:100px;top:224px;width:692px;height:379px}
.hero .hero-photo{width:692px;height:340px;background:linear-gradient(180deg,#b89a6e 0%,#d9c7a4 30%,#e9ebe8 55%,#8e8c86 85%,#6a6a66 100%)}
.hero .hero-caption{height:39px;background:var(--red);color:var(--white);display:flex;align-items:center;justify-content:space-between;padding:0 22px 0 32px;font-family:"Roboto Slab",serif;font-size:20px}
.hero .slider-arrows{display:flex;gap:8px}
.hero .slider-arrows span{width:26px;height:26px;border-radius:50%;background:var(--white);display:flex;align-items:center;justify-content:center}

.lead-form{position:absolute;left:792px;top:171px;width:314px;height:432px;background:var(--navy-panel);overflow:hidden}
.lead-form .form-cap{position:absolute;left:-20px;top:-30px;width:354px;height:100px;background:var(--red);border-radius:0 0 50% 50%/0 0 40% 40%}
.lead-form .form-title{position:absolute;left:0;top:12px;width:314px;text-align:center;color:var(--white);font-family:"Open Sans",sans-serif;font-weight:600;font-size:20px}
.lead-form .field{position:absolute;height:38px;background:var(--white);color:#222;font-family:"Lato",sans-serif;font-size:14px;display:flex;align-items:center;padding-left:13px}
.lead-form .submit{position:absolute;left:45px;top:372px;width:219px;height:42px;background:var(--red);color:var(--white);font-family:"Lato",sans-serif;font-weight:700;font-size:16px;display:flex;align-items:center;justify-content:center}

.content{position:absolute;left:100px;top:603px;width:1009px;height:1512px;background:var(--white)}

.how-it-works{position:absolute;left:0;top:0;width:1009px;height:299px;border-left:1px solid var(--line);border-right:1px solid var(--line)}
.section-title{font-family:"Roboto Slab",serif;font-weight:500;color:var(--blue)}
.how-it-works h2{position:absolute;top:24px;width:100%;text-align:center;font-size:25px}
.step{position:absolute;top:98px;width:240px;text-align:center}
.step svg{display:block;margin:0 auto}
.step h3{margin-top:22px;font-family:"Roboto Slab",serif;font-weight:500;font-size:18px;color:var(--red)}
.step p{margin:15px auto 0;width:220px;font-family:Arial,sans-serif;font-weight:700;font-size:12px;line-height:17px;letter-spacing:.6px;color:var(--text-grey)}
.step-arrow{position:absolute;top:113px}

.why-donate{position:absolute;left:0;top:299px;width:1009px;height:677px;background:var(--blue-section)}
.why-list{position:absolute;left:32px;top:40px;width:640px;color:var(--white)}
.why-list h2{font-family:"Roboto Slab",serif;font-weight:500;font-size:26px;margin-bottom:24px}
.why-list h3{font-family:"Open Sans",sans-serif;font-weight:700;font-size:17px;margin-top:12px}
.why-list p{font-family:Arial,sans-serif;font-size:13px;font-weight:700;letter-spacing:.5px;line-height:18px;margin-top:14px}

.side-box{position:absolute;left:695px;width:287px;background:var(--white);border:1px solid #c9dbe8}
.side-box.checklist{top:15px;height:248px;padding:20px 20px}
.side-box.checklist h3{font-family:"Roboto Slab",serif;font-weight:500;font-size:20px;color:var(--blue);text-align:center}
.side-box.checklist ul{list-style:none;margin-top:32px}
.side-box.checklist li{position:relative;padding-left:16px;font-family:Arial,sans-serif;font-size:12.5px;font-weight:700;color:#1a2a5a;line-height:16px;margin-bottom:7px}
.side-box.checklist li::before{content:"";position:absolute;left:0;top:3px;width:9px;height:9px;border-radius:50%;background:var(--blue)}
.side-box.call-box{top:278px;height:248px;text-align:center}
.side-box.call-box .call-icon{margin:40px auto 0;width:68px;height:68px;background:var(--red);border-radius:10px;display:flex;align-items:center;justify-content:center}
.side-box.call-box p{margin-top:24px;font-family:"Roboto Slab",serif;font-weight:500;font-size:24px;line-height:36px;color:var(--blue)}
.side-box.badges{top:544px;height:112px;display:flex}
.side-box.badges .badge{flex:1;display:flex;align-items:center;justify-content:center}
.side-box.badges .badge + .badge{border-left:1px solid var(--line)}

.faq{position:absolute;left:0;top:976px;width:1009px;height:536px;padding:0 32px;border-left:1px solid var(--line);border-right:1px solid var(--line)}
.faq h2{position:absolute;left:32px;top:40px;font-size:26px}
.faq-item{position:absolute;left:32px;width:900px}
.faq-item h3{font-family:"Roboto Slab",serif;font-weight:500;font-size:27px;color:var(--red)}
.faq-item p{margin-top:12px;font-family:Arial,sans-serif;font-weight:700;font-size:14.5px;letter-spacing:.7px;line-height:23.5px;color:var(--text-dark)}

.site-footer{position:absolute;left:0;top:2115px;width:1200px;height:152px;background:var(--footer);color:var(--white);font-family:"Open Sans",sans-serif;font-size:14.5px;letter-spacing:1px}
.site-footer .legal{position:absolute;left:100px;top:84px;display:flex}
.site-footer .legal span + span{margin-left:14px;padding-left:14px;border-left:1px solid rgba(255,255,255,.7)}
.site-footer .social{position:absolute;right:90px;top:74px;display:flex;align-items:center;gap:12px;letter-spacing:0}
.site-footer .social .dot{width:34px;height:34px;border-radius:50%}
.site-footer .social .dot.one{background:#2f4e93}
.site-footer .social .dot.two{background:#2bb6e6}
</style>
</head>
<body>

<header class="top-bar">
  <div class="help-links"><span>WE NEED YOUR HELP</span><span>Get Started</span></div>
  <div class="call">
    <span class="phone-box"><svg width="16" height="16" viewBox="0 0 24 24"><path d="M6.6 10.8a15.1 15.1 0 006.6 6.6l2.2-2.2a1 1 0 011-.25 11.4 11.4 0 003.6.6 1 1 0 011 1V20a1 1 0 01-1 1A17 17 0 013 4a1 1 0 011-1h3.5a1 1 0 011 1 11.4 11.4 0 00.6 3.6 1 1 0 01-.25 1z" fill="#0a2259"/></svg></span>
    <span>Call 1-800-555-0142</span>
  </div>
</header>

<div class="brand"><span class="brand-mark"></span><span class="brand-name">Autos for Patriots</span></div>
<div class="hours">Live Operations Available<br>7 Days A Week</div>

<nav class="main-nav"><a href="#">HOME</a><a href="#">ABOUT US</a><a href="#">GET STARTED</a></nav>

<section class="hero">
  <div class="hero-photo" role="img" aria-label="Photo of white donated vans parked in front of a building"></div>
  <div class="hero-caption">
    <span>Donate Your Car: Full Tax Deduction - Running or Not</span>
    <span class="slider-arrows">
      <span><svg width="12" height="12" viewBox="0 0 12 12"><path d="M8 1L3 6l5 5" stroke="#333" stroke-width="2.2" fill="none"/></svg></span>
      <span><svg width="12" height="12" viewBox="0 0 12 12"><path d="M4 1l5 5-5 5" stroke="#333" stroke-width="2.2" fill="none"/></svg></span>
    </span>
  </div>
</section>

<form class="lead-form">
  <div class="form-cap"></div>
  <div class="form-title">PLEASE FILL OUT FORM</div>
  <div class="field" style="left:30px;top:89px;width:124px">First Name</div>
  <div class="field" style="left:157px;top:89px;width:124px">Last Name</div>
  <div class="field" style="left:30px;top:145px;width:248px">Phone Number</div>
  <div class="field" style="left:30px;top:201px;width:248px">Type Your Email</div>
  <div class="field" style="left:30px;top:258px;width:124px">Zip Code</div>
  <div class="field" style="left:157px;top:258px;width:124px">Make of Car</div>
  <div class="field" style="left:30px;top:313px;width:124px">Model of Car</div>
  <div class="field" style="left:157px;top:313px;width:124px">Year of Car</div>
  <div class="submit">Click to Donate your Car</div>
</form>

<main class="content">
  <section class="how-it-works">
    <h2 class="section-title">How It Works</h2>

    <div class="step" style="left:26px">
      <svg width="52" height="58" viewBox="0 0 52 58"><rect x="4" y="6" width="44" height="50" rx="3" fill="none" stroke="#1a75bb" stroke-width="3"/><rect x="16" y="1" width="20" height="9" rx="2" fill="#1a75bb"/><path d="M13 24l3 3 5-6M13 36l3 3 5-6M13 48l3 3 5-6" stroke="#1a75bb" stroke-width="2" fill="none"/><path d="M26 25h14M26 37h14M26 49h14" stroke="#1a75bb" stroke-width="2"/></svg>
      <h3>Fill out the simple form</h3>
      <p>Lorem Ipsum has been the industry's standard dummy text ever since the 1500s,</p>
    </div>

    <svg class="step-arrow" style="left:303px" width="50" height="32" viewBox="0 0 50 32"><path d="M0 9h28V0l22 16-22 16v-9H0z" fill="#a3150f"/></svg>

    <div class="step" style="left:394px">
      <svg width="72" height="58" viewBox="0 0 72 58"><rect x="2" y="24" width="42" height="20" rx="2" fill="#1a75bb"/><path d="M44 20h14l10 12v12H44z" fill="#1a75bb"/><rect x="49" y="24" width="9" height="8" fill="#fff"/><path d="M10 24L30 4M30 4v12" stroke="#1a75bb" stroke-width="3" fill="none"/><circle cx="14" cy="48" r="7" fill="#1a75bb" stroke="#fff" stroke-width="2"/><circle cx="56" cy="48" r="7" fill="#1a75bb" stroke="#fff" stroke-width="2"/></svg>
      <h3>Schedule your free pick-up</h3>
      <p>Lorem Ipsum has been the industry's standard dummy text ever since the 1500s,</p>
    </div>

    <svg class="step-arrow" style="left:677px" width="50" height="32" viewBox="0 0 50 32"><path d="M0 9h28V0l22 16-22 16v-9H0z" fill="#a3150f"/></svg>

    <div class="step" style="left:752px">
      <svg width="56" height="60" viewBox="0 0 56 60"><path d="M4 4h26l10 10v34H4z" fill="#1a75bb"/><path d="M12 22h20M12 30h16M12 38h12" stroke="#fff" stroke-width="2.5"/><circle cx="38" cy="42" r="15" fill="#1a75bb" stroke="#fff" stroke-width="3"/><text x="38" y="49" text-anchor="middle" font-family="Arial,sans-serif" font-weight="700" font-size="19" fill="#fff">$</text></svg>
      <h3>Receive tax deduction</h3>
      <p>Lorem Ipsum has been the industry's standard dummy text ever since the 1500s,</p>
    </div>
  </section>

  <section class="why-donate">
    <div class="why-list">
      <h2>Why Donate Your Car to Us?</h2>
      <h3>IRS 501(c)3 Approved:</h3>
      <p>Free 24/7 Pickup with No DMV Hassles.</p>
      <h3>Free Local Towing to You:</h3>
      <p>We will pick up your car donation, running or not, when it's most convenient,<br>at home or work.</p>
      <h3>All Cars Accepted:</h3>
      <p>We take your car regardless of its condition or registration status.</p>
      <h3>Income Tax Deduction:</h3>
      <p>We issue you an IRS tax receipt &amp; offer the largest resale network to get you the highest tax write-off possible.</p>
      <h3>No Paperwork Hassles:</h3>
      <p>We take any car and handle everything: DMV, Smog and IRS paperwork.</p>
      <h3>Car donations help fund programs:</h3>
      <p>And benefit Hometown Heroes Relief Fund. An IRS 501(c)3 nonprofit organization.</p>
      <h3>Schedule a Free Pickup:</h3>
      <p>Complete the form and a representative will call you to arrange a convenient time to pickup your car.</p>
    </div>

    <aside class="side-box checklist">
      <h3>Donate Your Car Today!</h3>
      <ul>
        <li>You have no costs.</li>
        <li>Free towing, running or not.</li>
        <li>We issue you an IRS tax receipt.</li>
        <li>We take care of all paperwork.</li>
        <li>And we take care of DMV &amp; Smog issues.</li>
      </ul>
    </aside>

    <aside class="side-box call-box">
      <div class="call-icon"><svg width="38" height="38" viewBox="0 0 24 24"><path d="M6.6 10.8a15.1 15.1 0 006.6 6.6l2.2-2.2a1 1 0 011-.25 11.4 11.4 0 003.6.6 1 1 0 011 1V20a1 1 0 01-1 1A17 17 0 013 4a1 1 0 011-1h3.5a1 1 0 011 1 11.4 11.4 0 00.6 3.6 1 1 0 01-.25 1z" fill="#fff"/></svg></div>
      <p>We need your help<br>Call 1-800-555-0142</p>
    </aside>

    <aside class="side-box badges">
      <div class="badge"><svg width="96" height="96" viewBox="0 0 96 96" role="img" aria-label="Approved charity badge"><circle cx="48" cy="48" r="44" fill="#2a8fc9"/><circle cx="48" cy="48" r="32" fill="#e8f2f9"/></svg></div>
      <div class="badge"><svg width="120" height="60" viewBox="0 0 120 60" role="img" aria-label="Security badge"><rect x="4" y="6" width="112" height="48" rx="6" fill="#c0242a"/></svg></div>
    </aside>
  </section>

  <section class="faq">
    <h2 class="section-title">Frequently Asked Questions</h2>
    <div class="faq-item" style="top:106px">
      <h3>General</h3>
      <p>Lorem Ipsum has been the industry's standard dummy text ever since the 1500s,<br>when an unknown printer took a galley of type and scrambled it to make a type specimen book. It has<br>survived not only five centuries, but also the leap into electronic typesetting, remaining essentially unchanged.</p>
    </div>
    <div class="faq-item" style="top:253px">
      <h3>Tax Deduction</h3>
      <p>Lorem Ipsum has been the industry's standard dummy text ever since the 1500s,<br>when an unknown printer took a galley of type and scrambled it to make a type specimen book. It has<br>survived not only five centuries, but also the leap into electronic typesetting, remaining essentially unchanged.</p>
    </div>
    <div class="faq-item" style="top:398px">
      <h3>Pick-Up</h3>
      <p>Lorem Ipsum has been the industry's standard dummy text ever since the 1500s,<br>when an unknown printer took a galley of type and scrambled it to make a type specimen book. It has<br>survived not only five centuries, but also the leap into electronic typesetting, remaining essentially unchanged.</p>
    </div>
  </section>
</main>

<footer class="site-footer">
  <div class="legal"><span>2017 Copyright AUTOS FOR PATRIOTS</span><span>PRIVACY POLICY</span></div>
  <div class="social"><span>Connect Us:</span><span class="dot one"></span><span class="dot two"></span></div>
</footer>

</body>
</html>
```